Board menu for "Pan Dorado" food truck

Summary
**********************************
We need a menu design for a food truck. The menu will be printed and placed in the food truck side, so that customers can read it while standing one or two meters away from it. The size of the printed menu should be (width x height): 108cm x 70cm. The food truck is located in Panama and the menu language is Spanish.

Menu Sections
**************************************
The menu is divided in the following 5 sections:

1. Main Courses: This section should take most of the menu space. There are 5 menu items in this section. Each item has a Name, Description, Picture, Price (of item alone), and Price (of item in combo). Please note that for all items, combo means adding one beverage and one side. The added price is $1.50 to make any main course a combo. So it might we better to say “make it a combo for +$1.50” versus say “alone $5.50, in combo $7.00”.

2. Side Orders: This section has 2 menu items. Each item has a Name and Price. There are no pictures for this section or items.

3. Soups: This section has a Picture and Description for the entire section plus 2 menu items. Each menu item has a Name and Price.

4. Bakery: This section has a Picture for the entire section plus 5 menu items. Each item has a Name and a Price.

5. Beverages: This section has 5 menu items. Each menu item has a Name and a Price. There are no pictures for this section or items.

Attachments
*******************************************
We are attaching a zip file with picture of the exterior of the food truck. The menu will go in the space between the food truck’s window and the light switch, leaving ample space between those boundaries and the menu. The trash can shown in the picture has been relocated so it will not obstruct the menu view.

The zip file also contains the pictures for the 5 menu items in the Main Courses section, the picture for the Soups section, and the picture for the Bakery section (the bakery picture is provided as a place holder. We will provide a better bakery picture to the winning design to replace this one). For information purposes, the zip file also contains the food truck logo. The logo will not go in the menu. The brand and social media icons will go elsewhere in the truck.

The zip file also contains the file “menu information.xlsx”. This file has the following sheets:

Sections: Contains a column with the section name in English and another one with the section name in Spanish (which should be used in the menu). For the Soups section, contains a column with the section’s Description and Picture Name. For the Bakery section, contains a column with the section’s Picture Name.

Main Courses: Contains a column for each of the following: Item Name, Item Description, Item Picture Name, Item Price, Item Price (in combo). Again, we leave it to the designer’s discretion to use +$1.50 (or similar) for the combo versus publishing the full combo price.

Side Orders: Contains columns for Item Name and Item Price.

Soups: Contains columns for Item Name and Item Price.

Bakery: Contains columns for Item Name and Item Price. In the case of the Donuts item, there is an addition column with the Available Flavors.

Beverages: Contains columns for Item Name and Item Price. In the case of the Sodas item, there is an additional column with the Available Flavors.

A note about file encoding: the excel file contains texts with Spanish language special characters. It is encoded in the Windows-1252 encoding which I think is the Excel default for Western European languages. For those having trouble with this encoding, I included a “menu information csv” folder in the zip file with all the sheets in csv format encoded using UTF-8.
Updates

Target Market(s)

The truck sells fast food to drivers commuting from Panama City to towns in the west of the city. The average customer is a middle-class professional with a car. The truck is located in one of our gas stations so most customers stop to fuel their cars and grab something to eat for the ride home.

Font styles to use
Sans Serif

Colors

Designer to choose colors to be used in the design.

Requirements
Must have
• We would like to make emphasis in the main courses. Since they required preparation, they are not displayed, unlike other items like bakery, soups and beverages that are always ready and displayed. Having their pictures and descriptions on the menu will allows the customer to quickly figure out what main courses are available.

```html
<!DOCTYPE html>
<html lang="es">
<head>
<meta charset="utf-8">
<title>Pan Dorado — Menú</title>
<link href="https://fonts.googleapis.com/css2?family=Roboto+Condensed:wght@400;700&display=swap" rel="stylesheet">
<style>
:root{
  --frame:#141414;
  --green:#7cc21f;
  --cream-top:#fffef4;
  --cream-bottom:#fbf3b2;
  --red:#e3261c;
  --orange:#f07a1e;
  --yellow:#ffec00;
  --ink:#222;
  --white:#fff;
  --page:#e9e9e6;
}
*{box-sizing:border-box;margin:0;padding:0}
html,body{width:1200px;height:1200px;overflow:hidden;background:var(--page)}
body{font-family:"Roboto Condensed",Arial,sans-serif;color:var(--ink);position:relative}
.menu{position:absolute;left:20px;top:224px;width:1160px;height:752px;background:var(--frame)}
.panel{position:absolute;top:15px;width:553px;height:722px;overflow:hidden}
.panel--left{left:15px;background:var(--white)}
.panel--right{left:592px;background:linear-gradient(#fffef6,var(--cream-bottom));border-bottom-right-radius:150px 330px}
.section-bar{position:absolute;left:0;width:100%;height:32px;background:var(--green);color:var(--white);font-weight:700;font-size:22px;line-height:32px;padding-left:27px}
.panel--left .section-bar{text-align:center;padding-left:0;font-size:26px;top:0}
.row{position:absolute;left:0;width:100%;height:171px;background:linear-gradient(var(--cream-top),var(--cream-bottom))}
.dish-name{position:absolute;left:26px;top:18px;width:228px;height:32px;background:linear-gradient(90deg,var(--red),var(--orange));color:var(--white);font-weight:700;font-size:22px;line-height:32px;text-align:center}
.dish-desc{position:absolute;left:29px;top:58px;width:222px;font-size:15.5px;line-height:16.5px;text-align:justify}
.photo{position:absolute;left:306px;top:17px;width:225px;height:137px;border-radius:16px}
.price{position:absolute;height:21px;border-radius:11px;background:var(--yellow);font-size:17px;line-height:21px;padding:0 7px;color:var(--ink)}
.price--solo{left:292px;top:10px}
.combo-tag{position:absolute;left:497px;top:124px;background:var(--red);color:var(--white);font-size:12px;font-weight:700;padding:0 3px;line-height:13px}
.price--combo{left:485px;top:137px;font-weight:700}
.item{position:absolute;left:27px;font-size:17px;line-height:20px}
.item-price{position:absolute;left:277px;background:var(--yellow);font-size:17px;line-height:19px;padding:0 2px}
.flavors{position:absolute;left:150px;color:var(--white);font-size:13px;line-height:14px}
.flavors b{display:block;color:var(--red);font-size:10px;line-height:11px}
.brand{position:absolute;left:1077px;top:697px;display:flex;align-items:center;gap:8px;color:var(--white);font-size:15px;font-weight:700}
.brand i{display:block;width:34px;height:34px;border:2px solid var(--white);border-radius:50%}
</style>
</head>
<body>
<main class="menu">
  <section class="panel panel--left">
    <div class="section-bar">Platos Principales</div>

    <article class="row" style="top:34px">
      <h2 class="dish-name">A La Peña</h2>
      <p class="dish-desc">Emparedado de queso americano y jamones variados en pan flauta, a la peña.</p>
      <div class="photo" role="img" aria-label="Foto del emparedado de jamón y queso" style="background:linear-gradient(135deg,#c77a3a,#e8b26a 50%,#b5322a)"></div>
      <span class="price price--solo">$ 2.50</span>
      <span class="combo-tag">Combo</span><span class="price price--combo">$ 4.00</span>
    </article>

    <article class="row" style="top:207px">
      <h2 class="dish-name">Bucopocotón</h2>
      <p class="dish-desc">Choripan de chorizo criollo jumbo con chimichurri de la casa en pan baguette.</p>
      <div class="photo" role="img" aria-label="Foto del choripán con chimichurri y papas" style="background:linear-gradient(135deg,#d4964e,#5e7a2c 45%,#c93a30)"></div>
      <span class="price price--solo">$ 3.00</span>
      <span class="combo-tag">Combo</span><span class="price price--combo">$ 4.50</span>
    </article>

    <article class="row" style="top:378px">
      <h2 class="dish-name">Mi Patacón</h2>
      <p class="dish-desc">Pollo, cebolla caramelizada y salsa de ajo con cilantro sobre cama de patacones.</p>
      <div class="photo" role="img" aria-label="Foto de patacones con pollo y salsa de ajo" style="background:radial-gradient(circle at 50% 55%,#e8dcc2,#d9a531 55%,#1f3f8a 80%)"></div>
      <span class="price price--solo">$ 3.25</span>
      <span class="combo-tag">Combo</span><span class="price price--combo">$ 4.75</span>
    </article>

    <article class="row" style="top:551px">
      <h2 class="dish-name">El Favorito</h2>
      <p class="dish-desc">Emparedado de pollo a la plancha, queso mozzarella, cebolla caramelizada, tomate y salsa ranch en pan baguette.</p>
      <div class="photo" role="img" aria-label="Foto del emparedado de pollo a la plancha" style="background:linear-gradient(135deg,#d9b98f,#e9ddd0 50%,#8a5a3a)"></div>
      <span class="price price--solo">$ 4.50</span>
      <span class="combo-tag">Combo</span><span class="price price--combo">$ 6.00</span>
    </article>
  </section>

  <section class="panel panel--right">
    <article class="row" style="top:0;background:transparent">
      <h2 class="dish-name" style="left:17px;top:17px">La Bochinchosa</h2>
      <p class="dish-desc" style="left:21px;top:52px;width:225px">1/2 libra de hamburguesa Angus, queso americano, cebolla caramelizada, tomate, bacon y salsa de la casa en pan de miel con semillas de amapola.</p>
      <div class="photo" role="img" aria-label="Foto de la hamburguesa con papas fritas" style="left:308px;top:17px;background:linear-gradient(135deg,#c98a3c,#f2f0ea 45%,#d6332a)"></div>
      <span class="price price--solo" style="left:300px;top:11px">$ 5.50</span>
      <span class="combo-tag" style="left:497px;top:126px">Combo</span><span class="price price--combo" style="left:485px;top:139px">$ 7.00</span>
    </article>

    <div class="section-bar" style="top:174px">Acompañamientos</div>
    <span class="item" style="top:217px">Papas Fritas</span><span class="item-price" style="top:218px">$ 1.00</span>
    <span class="item" style="top:239px">Patacones</span><span class="item-price" style="top:240px">$ 1.00</span>

    <div class="section-bar" style="top:272px">Sopas</div>
    <span class="item" style="top:322px">Sopa de Pollo con Arroz</span><span class="item-price" style="top:323px">$ 2.95</span>
    <span class="item" style="top:344px">Sopa de Lenteja y Carne con Arroz</span><span class="item-price" style="top:345px">$ 2.95</span>
    <div class="photo" role="img" aria-label="Foto de un vaso de sopa" style="left:366px;top:311px;width:136px;height:81px;border-radius:6px;background:linear-gradient(90deg,#e7d9c4,#c94a44 50%,#222)"></div>

    <div class="section-bar" style="top:399px">Pastelería</div>
    <p class="flavors" style="top:403px"><b>Available Flavors</b>Crema Pastelera, Fresa Manzana, Maracuyá</p>
    <span class="item" style="top:443px">Enchilada de Carne</span><span class="item-price" style="top:444px">$ 1.50</span>
    <span class="item" style="top:465px">Pastelito de Pollo</span><span class="item-price" style="top:466px">$ 1.25</span>
    <span class="item" style="top:487px">Pañuelo de Queso</span><span class="item-price" style="top:488px">$ 1.00</span>
    <span class="item" style="top:509px">Cañón de Guayaba</span><span class="item-price" style="top:510px">$ 0.85</span>
    <span class="item" style="top:531px">Donas Rellenas</span><span class="item-price" style="top:532px">$ 8.85</span>
    <div class="photo" role="img" aria-label="Foto de pastelitos horneados" style="left:366px;top:465px;width:136px;height:81px;border-radius:6px;background:radial-gradient(circle,#d9a15a,#a9642a 60%,#2a2a2a)"></div>

    <div class="section-bar" style="top:561px">Bebidas</div>
    <p class="flavors" style="top:564px"><b>Available Flavors</b>Cola Brisa, Brisa Cero, Chispa, Gotita Fresa, Gotita Manzana</p>
    <span class="item" style="top:605px">Chicheme Chorrerano (16oz)</span><span class="item-price" style="top:606px">$ 1.60</span>
    <span class="item" style="top:627px">Chica del día (16oz)</span><span class="item-price" style="top:628px">$ 1.00</span>
    <span class="item" style="top:649px">Sodas (12oz)</span><span class="item-price" style="top:650px">$ 1.00</span>
    <span class="item" style="top:671px">Agua (16oz)</span><span class="item-price" style="top:672px">$ 0.75</span>
    <span class="item" style="top:693px">Café de Altura (8oz)</span><span class="item-price" style="top:694px">$ 1.00</span>
  </section>

  <div class="brand">Pan Dorado<i></i></div>
</main>
</body>
</html>
```